Kelvo Auto - help to get me noticed

We not long ago tasked Pixel Harbour to design a logo for my business. I'm happy with the result so would like to have a business card designed as a follow up.

It's an Automotive service and repair business that offers the following -
- Servicing
- General repairs
- Brakes
- Detailing
- Integrity

Kelvo Automotive
Dallin Mereth
0471 926 317

Target Market(s)

Everyday people with the ability to reach out to corporate customers also.

Industry/Entity Type

Automotive

Contact Information for Business Card

Black card, logo, name and phone number on front. Other details on back of card.

```html
<!DOCTYPE html>
<html lang="en">
<head>
<meta charset="utf-8">
<title>Kelvo Automotive – Business Card</title>
<link href="https://fonts.googleapis.com/css2?family=Arimo:wght@400;700&family=Oswald:wght@600&display=swap" rel="stylesheet">
<style>
  :root {
    --backdrop: #1b1b1b;
    --card: #2a2727;
    --lime: #8fc31f;
    --divider: #6f9a1c;
    --ink: #ffffff;
    --ink-soft: #f2f2f2;
  }
  * { margin: 0; padding: 0; box-sizing: border-box; }
  html, body {
    width: 1200px;
    height: 900px;
    overflow: hidden;
    background: var(--backdrop);
  }
  .canvas {
    position: relative;
    width: 1200px;
    height: 900px;
    background: var(--backdrop);
    font-family: "Arimo", Arial, sans-serif;
  }
  .card {
    position: absolute;
    left: 250px;
    width: 700px;
    height: 400px;
    background: var(--card);
    box-shadow: 0 6px 18px rgba(0,0,0,0.45);
  }
  .card--front { top: 40px; }
  .card--back { top: 470px; }

  /* Front */
  .front-stack {
    position: absolute;
    inset: 0;
    display: flex;
    flex-direction: column;
    align-items: center;
    justify-content: center;
  }
  .brand-name {
    font-family: "Arimo", Arial, sans-serif;
    font-weight: 700;
    color: var(--lime);
    letter-spacing: 1px;
    white-space: nowrap;
  }
  .card--front .brand-name { font-size: 50px; margin-bottom: 22px; }
  .phone {
    font-family: "Oswald", "Arial Narrow", sans-serif;
    font-weight: 600;
    font-size: 38px;
    color: var(--ink);
    letter-spacing: 2px;
    line-height: 1;
  }
  .person {
    margin-top: 12px;
    font-weight: 700;
    font-size: 22px;
    color: var(--ink);
    letter-spacing: 2px;
    text-transform: uppercase;
  }

  /* Back */
  .back-layout {
    position: absolute;
    inset: 0;
    display: flex;
    align-items: center;
    padding-left: 60px;
  }
  .card--back .brand-name { font-size: 40px; width: 300px; line-height: 1.1; white-space: normal; }
  .divider {
    width: 2px;
    height: 170px;
    background: var(--divider);
    margin: 0 26px 0 20px;
  }
  .services {
    color: var(--ink-soft);
    font-size: 17px;
    line-height: 1.45;
  }
  .services-intro { margin-bottom: 8px; max-width: 300px; }
  .services-list { list-style: none; }
</style>
</head>
<body>
<main class="canvas">
  <section class="card card--front" aria-label="Card front">
    <div class="front-stack">
      <div class="brand-name">Kelvo Automotive</div>
      <div class="phone">0471 926 317</div>
      <div class="person">Dallin Mereth</div>
    </div>
  </section>

  <section class="card card--back" aria-label="Card back">
    <div class="back-layout">
      <div class="brand-name">Kelvo Automotive</div>
      <div class="divider"></div>
      <div class="services">
        <p class="services-intro">It's an Automotive service and repair business that offers the following :</p>
        <ul class="services-list">
          <li>Servicing</li>
          <li>General repairs</li>
          <li>Brakes</li>
          <li>Detailing</li>
          <li>Integrity</li>
        </ul>
      </div>
    </div>
  </section>
</main>
</body>
</html>
```